Professional Business Cards

We need a nice looking, profession and modern business card for our new company. Our logo is attatched

Target Market(s)

Young Professionals

Industry/Entity Type

Financial

Contact Information for Business Card

FRONT

Morvane Tally Pty Ltd
Level 22, Halden Court, 48 Wirrapool St
Sydney NSW 2000
ABN : 57 304 918 226

Derek Wallis - Chief Operations Officer
P : 02 7153 2819
M: 0418 395 207
derek@morvanetally,com

BACK

- Cryptocurrency Exchange Services
- Cryptocurrency Mining Operations
- Cryptocurrency Investment Fund Offering

Font styles to use
Sans Serif

Colors
0255a3
9d9d9d

```html
<!DOCTYPE html>
<html lang="en">
<head>
<meta charset="utf-8">
<title>Morvane Tally – Business Cards</title>
<link href="https://fonts.googleapis.com/css2?family=Roboto:ital,wght@0,400;0,500;0,700;1,400;1,700&display=swap" rel="stylesheet">
<style>
  :root {
    --brand-blue: #0255a3;
    --card-blue: #0f5aa8;
    --brand-grey: #9d9d9d;
    --paper: #ffffff;
    --pattern-tint: #eef0f7;
    --stage: #3a3b3d;
    --ink-light: #ffffff;
  }
  * { box-sizing: border-box; margin: 0; padding: 0; }
  html, body {
    width: 1200px; height: 900px; overflow: hidden;
    background: var(--stage);
    font-family: "Roboto", Arial, sans-serif;
  }
  .stage {
    position: relative; width: 1200px; height: 900px;
  }
  .card {
    position: absolute; left: 250px; width: 700px; height: 400px;
    border-radius: 26px; overflow: hidden;
    box-shadow: 0 10px 30px rgba(0,0,0,.35);
  }

  /* Back side */
  .card-back { top: 36px; background: var(--paper); }
  .back-pattern {
    position: absolute; inset: 0;
    background: linear-gradient(135deg, var(--paper) 0%, var(--pattern-tint) 100%);
  }
  .back-brand {
    position: absolute; left: 0; right: 0; top: 120px;
    display: flex; align-items: center; justify-content: center; gap: 16px;
  }
  .brand-square { width: 46px; height: 46px; background: var(--brand-blue); }
  .brand-name {
    font-weight: 700; font-size: 50px; letter-spacing: 2px;
    color: var(--brand-blue); text-transform: uppercase;
  }
  .back-rule {
    position: absolute; left: 70px; right: 70px; height: 1.5px;
    background: var(--brand-blue);
  }
  .back-rule.top { top: 210px; }
  .back-rule.bottom { top: 306px; }
  .services {
    position: absolute; left: 0; right: 0; top: 228px;
    text-align: center; color: var(--brand-blue);
    font-size: 19px; font-style: italic; font-weight: 500; line-height: 1.6;
  }
  .services .dot {
    display: inline-block; width: 7px; height: 7px; margin: 0 10px 3px;
    background: var(--brand-grey);
  }

  /* Front side */
  .card-front { top: 466px; background: var(--card-blue); color: var(--ink-light); }
  .notch {
    position: absolute; left: 0; top: 26px;
    width: 0; height: 0;
    border-top: 15px solid transparent; border-bottom: 15px solid transparent;
    border-left: 16px solid var(--ink-light);
  }
  .holder { position: absolute; left: 40px; top: 26px; }
  .holder-name {
    font-size: 24px; font-weight: 700; font-style: italic;
    text-transform: uppercase; letter-spacing: .5px;
  }
  .holder-title {
    font-size: 17px; font-style: italic; text-transform: uppercase; margin-top: 2px;
  }
  .front-brand {
    position: absolute; right: 40px; top: 130px;
    display: flex; align-items: center; gap: 14px;
  }
  .front-brand .brand-square { width: 40px; height: 40px; background: var(--ink-light); }
  .front-brand .brand-name { color: var(--ink-light); font-size: 42px; }
  .address {
    position: absolute; left: 40px; top: 220px;
    font-size: 16px; line-height: 1.45;
  }
  .front-rule {
    position: absolute; left: 40px; right: 40px; top: 300px; height: 1.5px;
    background: var(--ink-light);
  }
  .contacts {
    position: absolute; right: 40px; top: 310px;
    list-style: none; text-align: right; font-size: 18px; line-height: 1.5;
  }
  .contacts li { display: flex; justify-content: flex-end; align-items: center; gap: 12px; }
  .contacts svg { width: 20px; height: 20px; fill: none; stroke: var(--ink-light); stroke-width: 1.8; }
</style>
</head>
<body>
<main class="stage">

  <section class="card card-back" aria-label="Card back">
    <div class="back-pattern" role="img" aria-label="Faint repeating brand motif pattern"></div>
    <div class="back-brand">
      <span class="brand-square"></span>
      <span class="brand-name">Morvane Tally</span>
    </div>
    <div class="back-rule top"></div>
    <p class="services">
      Cryptocurrency Exchange Services<span class="dot"></span>Cryptocurrency Mining Operations<br>
      Cryptocurrency Investment Fund Offering
    </p>
    <div class="back-rule bottom"></div>
  </section>

  <section class="card card-front" aria-label="Card front">
    <span class="notch"></span>
    <div class="holder">
      <p class="holder-name">Derek Wallis</p>
      <p class="holder-title">Chief Operations Officer</p>
    </div>
    <div class="front-brand">
      <span class="brand-square"></span>
      <span class="brand-name">Morvane Tally</span>
    </div>
    <address class="address" style="font-style:normal">
      Level 22, Halden Court, 48 Wirrapool St<br>
      Sydney NSW 2000<br>
      ABN : 57 304 918 226
    </address>
    <div class="front-rule"></div>
    <ul class="contacts">
      <li>02.7153.2819
        <svg viewBox="0 0 24 24" aria-hidden="true"><path d="M5 4h4l2 5-2.5 1.5a11 11 0 0 0 5 5L15 13l5 2v4a2 2 0 0 1-2 2A16 16 0 0 1 3 6a2 2 0 0 1 2-2z"/></svg>
      </li>
      <li>0418.395.207
        <svg viewBox="0 0 24 24" aria-hidden="true"><rect x="6" y="2" width="12" height="20" rx="2"/><line x1="11" y1="18" x2="13" y2="18"/></svg>
      </li>
      <li>derek@morvanetally,com
        <svg viewBox="0 0 24 24" aria-hidden="true"><rect x="3" y="5" width="18" height="14" rx="1"/><path d="M3 6l9 7 9-7"/></svg>
      </li>
    </ul>
  </section>

</main>
</body>
</html>
```